Advertising company unique advertising platform

we need a logo design for a new company based in Australia Melbourne. We develop innovated advertising platform where consumer can use this platform to get regular discount, as business owner they can use this platform for free advertisement. Payment for this advertisement platform only payable every two weeks, when I generate revenue for their business

Industry/Entity Type

Advertising

Contact Information for Business Card

Dale Morrow | Co-Founder |Managing Director
Suite 318 274 Bramwell Lane Melbourne Vic 3000

ABN 62 914 305 718
Tel: +61 0491 258 307 | Email: dale.morrow@plovintarex.com

Font styles to use
Decorative
Script

Requirements
Must have
• Try few different design and some round corner business card
Should not have
• One round corner business card...try 4 different colour background not only black, make sure two side is designed. Be creative so imagine you are giving this to a client make sure has wow factor, if you can also try one design with engrave like all the logo, words look 3d feel
• The word Advertising Platform use attached file font

```html
<!DOCTYPE html>
<html lang="en">
<head>
<meta charset="utf-8">
<title>Brightway Market – Business Card</title>
<link rel="stylesheet" href="https://fonts.googleapis.com/css2?family=Open+Sans:wght@400;600;700&display=swap">
<style>
  :root {
    --backdrop: #d9d9d9;
    --card: #2a2a2a;
    --text: #f2f2f2;
    --text-soft: #e4e4e4;
    --accent: #f07a2a;
    --teal: #3fb8a8;
  }
  html, body {
    margin: 0;
    width: 1200px;
    height: 1200px;
    overflow: hidden;
    background: var(--backdrop);
    font-family: "Open Sans", Arial, sans-serif;
  }
  .canvas {
    width: 1200px;
    height: 1200px;
    display: flex;
    align-items: center;
    justify-content: center;
  }
  .business-card {
    position: relative;
    width: 1000px;
    height: 570px;
    background: var(--card);
    border-radius: 56px;
    box-shadow: 0 18px 40px rgba(0,0,0,0.25);
    color: var(--text);
  }
  .brand {
    position: absolute;
    left: 90px;
    top: 150px;
    display: flex;
    align-items: center;
    gap: 22px;
  }
  .brand-mark {
    width: 110px;
    height: 110px;
    border-radius: 50%;
    background: var(--accent);
    flex: none;
  }
  .brand-name {
    font-size: 46px;
    font-weight: 700;
    line-height: 1.1;
    color: var(--accent);
    width: 300px;
  }
  .person {
    position: absolute;
    left: 90px;
    top: 345px;
  }
  .person-name {
    font-size: 34px;
    font-weight: 700;
    margin: 0 0 6px;
  }
  .person-role {
    font-size: 22px;
    line-height: 1.4;
    margin: 0;
    color: var(--text-soft);
  }
  .contact-list {
    position: absolute;
    left: 560px;
    top: 160px;
    margin: 0;
    padding: 0;
    list-style: none;
    font-size: 22px;
    line-height: 1.35;
    color: var(--text-soft);
  }
  .contact-item {
    display: flex;
    align-items: flex-start;
    gap: 16px;
    margin-bottom: 20px;
  }
  .contact-icon {
    width: 22px;
    height: 22px;
    flex: none;
    margin-top: 4px;
  }
</style>
</head>
<body>
<main class="canvas">
  <section class="business-card">
    <div class="brand">
      <div class="brand-mark"></div>
      <div class="brand-name">Brightway Market</div>
    </div>

    <div class="person">
      <p class="person-name">Dale Morrow</p>
      <p class="person-role">Co-Founder | Managing Director<br>Founder &amp; Director</p>
    </div>

    <ul class="contact-list">
      <li class="contact-item">
        <svg class="contact-icon" viewBox="0 0 24 24" aria-hidden="true">
          <path fill="var(--accent)" d="M12 1a8 8 0 0 0-8 8c0 6 8 14 8 14s8-8 8-14a8 8 0 0 0-8-8zm0 11a3 3 0 1 1 0-6 3 3 0 0 1 0 6z"/>
        </svg>
        <span>Suite 318 274<br>Bramwell Lane<br>Melbourne Vic 3000</span>
      </li>
      <li class="contact-item">
        <svg class="contact-icon" viewBox="0 0 24 24" aria-hidden="true">
          <path fill="var(--accent)" d="M6.6 10.8a15 15 0 0 0 6.6 6.6l2.2-2.2a1 1 0 0 1 1-.25 11.4 11.4 0 0 0 3.6.57 1 1 0 0 1 1 1V20a1 1 0 0 1-1 1A17 17 0 0 1 3 4a1 1 0 0 1 1-1h3.5a1 1 0 0 1 1 1c0 1.25.2 2.45.57 3.6a1 1 0 0 1-.25 1z"/>
        </svg>
        <span>+61 0491 258 307</span>
      </li>
      <li class="contact-item">
        <svg class="contact-icon" viewBox="0 0 24 24" aria-hidden="true">
          <rect x="2" y="5" width="20" height="14" rx="1.5" fill="var(--accent)"/>
          <path d="M3 6l9 7 9-7" fill="none" stroke="var(--card)" stroke-width="1.6"/>
        </svg>
        <span>dale.morrow@plovintarex.com</span>
      </li>
      <li class="contact-item">
        <svg class="contact-icon" viewBox="0 0 24 24" aria-hidden="true">
          <circle cx="12" cy="12" r="10" fill="var(--accent)"/>
          <path d="M2 12h20M12 2c3 3 3 17 0 20M12 2c-3 3-3 17 0 20" fill="none" stroke="var(--card)" stroke-width="1.4"/>
        </svg>
        <span>www.plovintarex.com</span>
      </li>
    </ul>
  </section>
</main>
</body>
</html>
```